RJ Heating & Cooling / 2018 Varden Kestrel Medium Roof / 148"wb

Customer is looking for a new design on his new 2018 varden kestrel medium roof 148"wb van. This will be a Full Wrap.

Attached is: >Customers logo
> Template for the van he has (You don't have to use this exact one for the proof)

Please include: > Slogan- Quality work at reasonable prices
>(555) 014-2293
>Services- Repairs, installation, maintenance, water heaters, indoor air quality
>Residential & Commercial

```html
<!DOCTYPE html>
<html lang="en">
<head>
<meta charset="utf-8">
<title>RJ Heating &amp; Cooling – Varden Kestrel Full Wrap</title>
<link href="https://fonts.googleapis.com/css2?family=Montserrat:ital,wght@0,500;0,700;0,800;1,500;1,700&family=Lora:ital,wght@1,500&display=swap" rel="stylesheet">
<style>
  :root{
    --bg:#e4e4e6;
    --white:#f6f6f7;
    --orange:#ee6a12;
    --orange-deep:#e0480f;
    --gold:#f4a21a;
    --sky:#5aa1db;
    --navy:#1f3f8f;
    --ink:#2a2a2e;
  }
  html,body{margin:0;padding:0;}
  body{
    width:1200px;height:3419px;overflow:hidden;
    background:var(--bg);
    font-family:"Montserrat",sans-serif;
  }
  .sheet{position:relative;width:1200px;height:3419px;}
  .panel{position:absolute;display:block;}
  .panel--side-driver{left:40px;top:210px;width:1120px;height:460px;}
  .panel--side-passenger{left:40px;top:1100px;width:1120px;height:460px;}
  .panel--rear{left:290px;top:1880px;width:620px;height:560px;}
  .panel--hood{left:300px;top:2840px;width:600px;height:220px;}

  .services{font-family:"Montserrat",sans-serif;font-weight:700;font-size:20px;fill:#fff;}
  .services--italic{font-style:italic;}
  .brand-name{font-family:"Montserrat",sans-serif;font-weight:800;fill:var(--orange);}
  .slogan{font-family:"Lora",serif;font-style:italic;font-weight:500;}
  .sector{font-family:"Montserrat",sans-serif;font-weight:500;}
  .phone{font-family:"Montserrat",sans-serif;font-weight:700;}
</style>
</head>
<body>
<main class="sheet">

  <!-- Driver side: cab at right -->
  <svg class="panel panel--side-driver" viewBox="0 0 1120 460" aria-label="Driver side wrap">
    <defs>
      <linearGradient id="orangeSide" x1="0" y1="0" x2="0" y2="1">
        <stop offset="0" stop-color="var(--gold)"/>
        <stop offset="0.35" stop-color="var(--orange)"/>
        <stop offset="1" stop-color="var(--orange-deep)"/>
      </linearGradient>
    </defs>
    <rect class="body-base" x="0" y="0" width="1120" height="460" rx="40" fill="var(--white)"/>
    <path class="orange-field" d="M0 40 Q0 0 40 0 H330 L490 150 L300 270 L0 300 Z" fill="url(#orangeSide)"/>
    <path class="blue-swoosh" d="M300 270 L830 345 L1120 330 L1120 380 L0 410 L0 300 Z" fill="var(--sky)"/>
    <path class="orange-stripe" d="M560 300 L1120 300 L1120 322 L760 318 Z" fill="var(--orange-deep)"/>
    <path class="navy-stripe" d="M300 430 L1120 405 L1120 420 L300 450 Z" fill="var(--navy)"/>
    <path class="lower-trim" d="M0 410 L1120 380 L1120 420 Q1120 460 1080 460 H40 Q0 460 0 420 Z" fill="var(--ink)" opacity=".85"/>
    <g class="services">
      <text x="110" y="90">› Services</text>
      <text x="110" y="116">› Repairs</text>
      <text x="110" y="142">› installation</text>
      <text x="110" y="168">› Maintenance</text>
      <text x="110" y="194">› water heaters</text>
      <text x="110" y="220">› indoor air quality</text>
    </g>
    <text class="brand-name" x="520" y="150" font-size="46">RJ Heating</text>
    <text class="brand-name" x="560" y="200" font-size="46">&amp; Cooling</text>
    <g transform="rotate(8 320 300)">
      <text class="slogan" x="320" y="300" font-size="26" fill="var(--orange-deep)">Quality Work at reasonable prices !</text>
      <text class="sector" x="380" y="322" font-size="15" fill="var(--navy)">Residential &amp; Commercial</text>
    </g>
    <text class="phone" x="750" y="260" font-size="30" fill="var(--navy)" transform="rotate(5 750 260)">(555) 014-2293</text>
  </svg>

  <!-- Passenger side: cab at left -->
  <svg class="panel panel--side-passenger" viewBox="0 0 1120 460" aria-label="Passenger side wrap">
    <defs>
      <linearGradient id="orangeSide2" x1="0" y1="0" x2="0" y2="1">
        <stop offset="0" stop-color="var(--gold)"/>
        <stop offset="0.35" stop-color="var(--orange)"/>
        <stop offset="1" stop-color="var(--orange-deep)"/>
      </linearGradient>
    </defs>
    <rect class="body-base" x="0" y="0" width="1120" height="460" rx="40" fill="var(--white)"/>
    <g transform="translate(1120 0) scale(-1 1)">
      <path class="orange-field" d="M0 40 Q0 0 40 0 H330 L490 150 L300 270 L0 300 Z" fill="url(#orangeSide2)"/>
      <path class="blue-swoosh" d="M300 270 L830 345 L1120 330 L1120 380 L0 410 L0 300 Z" fill="var(--sky)"/>
      <path class="orange-stripe" d="M560 300 L1120 300 L1120 322 L760 318 Z" fill="var(--orange-deep)"/>
      <path class="navy-stripe" d="M300 430 L1120 405 L1120 420 L300 450 Z" fill="var(--navy)"/>
      <path class="lower-trim" d="M0 410 L1120 380 L1120 420 Q1120 460 1080 460 H40 Q0 460 0 420 Z" fill="var(--ink)" opacity=".85"/>
    </g>
    <g class="services">
      <text x="860" y="90">› Services</text>
      <text x="860" y="116">› Repairs</text>
      <text x="860" y="142">› installation</text>
      <text x="860" y="168">› Maintenance</text>
      <text x="860" y="194">› water heaters</text>
      <text x="860" y="220">› indoor air quality</text>
    </g>
    <text class="brand-name" x="320" y="150" font-size="46">RJ Heating</text>
    <text class="brand-name" x="360" y="200" font-size="46">&amp; Cooling</text>
    <g transform="rotate(-8 360 358)">
      <text class="slogan" x="360" y="358" font-size="26" fill="var(--orange-deep)">Quality Work at reasonable prices !</text>
      <text class="sector" x="420" y="380" font-size="15" fill="var(--navy)">Residential &amp; Commercial</text>
    </g>
    <text class="phone" x="200" y="290" font-size="30" fill="var(--orange-deep)" transform="rotate(-5 200 290)">(555) 014-2293</text>
  </svg>

  <!-- Rear doors -->
  <svg class="panel panel--rear" viewBox="0 0 620 560" aria-label="Rear doors wrap">
    <defs>
      <linearGradient id="orangeRear" x1="0" y1="0" x2="1" y2="0">
        <stop offset="0" stop-color="var(--orange-deep)"/>
        <stop offset="0.6" stop-color="var(--orange)"/>
        <stop offset="1" stop-color="var(--gold)"/>
      </linearGradient>
    </defs>
    <rect class="body-base" x="0" y="0" width="620" height="560" rx="30" fill="var(--white)"/>
    <path class="blue-wedge" d="M0 30 Q0 0 30 0 H110 L240 130 L0 260 Z" fill="var(--sky)"/>
    <path class="blue-band" d="M0 270 L620 310 L620 360 L0 320 Z" fill="var(--sky)"/>
    <path class="navy-edge" d="M0 262 L180 272 L0 290 Z" fill="var(--navy)"/>
    <path class="orange-field" d="M0 320 L620 360 L620 530 Q620 560 590 560 H30 Q0 560 0 530 Z" fill="url(#orangeRear)"/>
    <line class="door-split" x1="310" y1="0" x2="310" y2="560" stroke="var(--ink)" stroke-width="2" opacity=".6"/>
    <text class="brand-name" x="290" y="140" font-size="42">RJ Heating</text>
    <text class="brand-name" x="330" y="188" font-size="42">&amp; Cooling</text>
    <text class="slogan" x="150" y="313" font-size="22" fill="#fff" transform="rotate(3.7 150 313)">Quality Work at reasonable prices</text>
    <g class="services services--italic">
      <text x="55" y="412">› Services</text>
      <text x="55" y="438">› Repairs</text>
      <text x="55" y="464">› installation</text>
      <text x="55" y="490">› Maintenance</text>
      <text x="55" y="516">› water heaters</text>
      <text x="55" y="542">› indoor air quality</text>
    </g>
    <text class="phone" x="330" y="470" font-size="32" fill="var(--navy)">(555) 014-2293</text>
    <text class="sector" x="355" y="496" font-size="17" font-style="italic" fill="#fff">Residential &amp; Commercial</text>
  </svg>

  <!-- Hood -->
  <svg class="panel panel--hood" viewBox="0 0 600 220" aria-label="Hood wrap">
    <path class="hood-base" d="M40 20 Q300 -10 560 20 L600 200 Q300 230 0 200 Z" fill="var(--white)"/>
    <text class="brand-name" x="300" y="120" font-size="40" text-anchor="middle">RJ Heating &amp; Cooling</text>
  </svg>

</main>
</body>
</html>
```